Business card for a young aspring actress

My daughter is 18 and just starting out on her profession as an actress. She is a member of the Harbour Young Players and has already had some extras work and a featured role in an upcoming Feature film.

She wants/needs a card that she can have to hand to give to those she comes into contact with in the theatre, TV and film industries.

We are thinking that it may be double sided with an impact side including a picture of her and her name etc with the reverse holding contact and other details.

She wants to go by the name Maya Louise Brennick.

She has done a little modelling but sees herself as an actress.

She can be seen in this video
http://www.oakvalepark-academy.org/videos/be0881e4276ee2512c50a07f907c1d03?width=640&height=480

Target Market(s)

Anyone she comes into contact with in theatre TV and film industries.

Industry/Entity Type

Business

Requirements
Nice to have
• She has email and a website www.mayabrennick.com She is quite a connected girl

```html
<!DOCTYPE html>
<html lang="en">
<head>
<meta charset="utf-8">
<title>Maya Louise Brennick — Business Card</title>
<link rel="stylesheet" href="https://fonts.googleapis.com/css2?family=Oxanium:wght@300;400&family=Quicksand:wght@500&display=swap">
<style>
  :root {
    --page-bg: #e9e7e2;
    --card-front-grey: #3a3a3a;
    --card-black: #060606;
    --name-box: #070707;
    --gold: #c9a54a;
    --photo-light: #e2e4e6;
    --photo-mid: #9a9ea2;
    --photo-dark: #2c2d2f;
  }
  * { margin: 0; padding: 0; box-sizing: border-box; }
  html, body {
    width: 1200px;
    height: 1000px;
    overflow: hidden;
    background: var(--page-bg);
  }
  .canvas {
    position: relative;
    width: 1200px;
    height: 1000px;
  }
  .card {
    position: absolute;
    top: 190px;
    width: 400px;
    height: 620px;
    overflow: hidden;
    box-shadow: 0 10px 30px rgba(0,0,0,0.18);
  }

  /* Front: portrait side */
  .card-front {
    left: 185px;
    background: var(--card-front-grey);
    border-radius: 170px 0 170px 0;
  }
  .portrait {
    position: absolute;
    inset: 0;
    width: 400px;
    height: 620px;
  }
  .name-box {
    position: absolute;
    left: 170px;
    top: 290px;
    width: 230px;
    height: 150px;
    background: var(--name-box);
    display: flex;
    align-items: center;
    justify-content: flex-end;
    padding-right: 18px;
  }
  .name {
    font-family: "Oxanium", sans-serif;
    font-weight: 300;
    color: var(--gold);
    text-transform: uppercase;
    letter-spacing: 0.12em;
    line-height: 1.2;
    font-size: 22px;
  }
  .name-box .name { text-align: right; }

  /* Back: contact side */
  .card-back {
    left: 615px;
    background: radial-gradient(ellipse 140% 80% at 75% 0%, #2a2d30 0%, #0d0e0f 45%, var(--card-black) 70%);
    border-radius: 0 170px 0 170px;
  }
  .card-back .name {
    position: absolute;
    left: 30px;
    top: 110px;
    text-align: left;
  }
  .contact {
    position: absolute;
    right: 30px;
    bottom: 45px;
    list-style: none;
    text-align: right;
    font-family: "Quicksand", sans-serif;
    font-weight: 500;
    font-size: 16px;
    color: var(--gold);
    letter-spacing: 0.04em;
  }
  .contact li { line-height: 30px; }
  .contact .phone + .email { margin-top: 8px; }
</style>
</head>
<body>
<main class="canvas">

  <section class="card card-front">
    <svg class="portrait" viewBox="0 0 400 620" role="img" aria-label="Black and white portrait photograph of the actress with long straight hair">
      <defs>
        <linearGradient id="portraitTone" x1="0" y1="0" x2="1" y2="0.3">
          <stop offset="0" stop-color="var(--photo-light)"/>
          <stop offset="0.55" stop-color="var(--photo-mid)"/>
          <stop offset="1" stop-color="var(--photo-dark)"/>
        </linearGradient>
      </defs>
      <path d="M0 0 H165 V320 C165 460 220 550 320 620 H0 Z" fill="url(#portraitTone)"/>
    </svg>
    <div class="name-box">
      <p class="name">Maya<br>Louise<br>Brennick</p>
    </div>
  </section>

  <section class="card card-back">
    <p class="name">Maya<br>Louise<br>Brennick</p>
    <ul class="contact">
      <li class="phone">+44 7700 900318</li>
      <li class="phone">+44 20 7946 0542</li>
      <li class="email">maya@mayabrennick.com</li>
      <li class="web">www.mayabrennick.com</li>
    </ul>
  </section>

</main>
</body>
</html>
```